Marlowick APP redesign and color change

I am looking for a new design for my app. Please see the attached current design.

Currently, I have a functioning app but the colors and design are awful!
The logo is great but the rest of the app needs a refresh.
(Logo hi res not yet available but will upload soon.)
New colors or anything that is cutting edge.

Basically: It is a secure social media app within a school system where the teachers, students and parents can text, exchange photos, plan curriculum, etc.

I NEED ONLY landing page with a new look!
Looking for one distinct design for the landing page with new look.
The developer will apply this one design towards the rest of the pages/app screens.

Because part of the social media I need the feel and look of what is now the trend. Something that will attract and keep the client(s) interested. I am really leaving all the creative work to the designer and open to any suggestions.
Updates

Target Market(s)

Schools, community, teachers, students, colleges, sport teams

Industry/Entity Type

Non Profit

Font styles to use
Serif
Sans Serif

Colors

Designer to choose colors to be used in the design.

Requirements
Must have
• Sharp, trendy, millennial feel
Nice to have
• Up to designer
Should not have
• Up to designer

```html
<!DOCTYPE html>
<html lang="en">
<head>
<meta charset="utf-8">
<title>Marlowick — Landing</title>
<link href="https://fonts.googleapis.com/css2?family=Fira+Sans:wght@400;500&family=Raleway:wght@400;500&display=swap" rel="stylesheet">
<style>
  :root {
    --brand-blue: #0066e0;
    --screen-blue-top: #1238c8;
    --screen-blue-bottom: #0a2aa8;
    --ink: #111111;
    --ink-soft: #333333;
    --white: #ffffff;
    --phone-body: #f4f5f7;
    --phone-edge: #d5d8dd;
  }
  * { box-sizing: border-box; margin: 0; padding: 0; }
  html, body { width: 1200px; height: 750px; overflow: hidden; background: var(--white); }
  .page { position: relative; width: 1200px; height: 750px; overflow: hidden; font-family: "Fira Sans", sans-serif; }

  .topbar { position: absolute; top: 0; left: 0; width: 1200px; height: 83px; background: var(--brand-blue); display: flex; align-items: center; z-index: 3; }
  .brand { position: absolute; left: 97px; display: flex; align-items: center; gap: 8px; color: var(--white); font-size: 17px; font-weight: 500; }
  .brand-dot { width: 16px; height: 16px; border-radius: 50%; background: var(--white); }
  .nav { position: absolute; left: 238px; display: flex; gap: 25px; list-style: none; }
  .nav a { color: var(--white); text-decoration: none; font-size: 15px; opacity: .92; }
  .nav a.is-current { font-weight: 500; opacity: 1; }

  .hero-photo { position: absolute; top: 83px; left: 0; width: 1200px; height: 667px;
    background: linear-gradient(100deg, #c9b8a6 0%, #8d7fa8 20%, #b2463f 38%, #e3c99a 52%, #9fc4a6 64%, #c9c3bc 80%, #9db2b6 100%); }
  .hero-fade { position: absolute; top: 83px; left: 597px; width: 603px; height: 667px; background: rgba(255,255,255,.72); }

  .hero-copy { position: absolute; left: 668px; top: 268px; width: 400px; font-family: "Raleway", sans-serif; font-size: 25px; line-height: 30px; color: var(--ink); }
  .btn { position: absolute; display: flex; align-items: center; justify-content: center; width: 200px; height: 55px; border-radius: 3px; font-family: "Raleway", sans-serif; font-size: 23px; text-decoration: none; }
  .btn-login { left: 816px; top: 395px; background: var(--brand-blue); color: var(--white); }
  .btn-signup { left: 818px; top: 527px; background: var(--white); color: var(--ink-soft); border: 2px solid #e6e6e6; }
  .signup-hint { position: absolute; left: 816px; top: 497px; width: 200px; text-align: center; font-family: "Raleway", sans-serif; font-size: 14px; color: var(--ink-soft); }

  .phone { position: absolute; left: 479px; top: 385px; width: 232px; height: 400px; background: var(--phone-body); border: 2px solid var(--phone-edge); border-radius: 36px; }
  .phone-cam { position: absolute; left: 77px; top: 26px; width: 7px; height: 7px; border-radius: 50%; background: #222; }
  .phone-dot { position: absolute; left: 111px; top: 11px; width: 5px; height: 5px; border-radius: 50%; background: #222; }
  .phone-speaker { position: absolute; left: 98px; top: 27px; width: 36px; height: 3px; border-radius: 2px; background: #222; }
  .screen { position: absolute; left: 11px; top: 55px; width: 208px; height: 360px; background: linear-gradient(180deg, var(--screen-blue-top), var(--screen-blue-bottom)); border: 2px solid #111; color: var(--white); }
  .status { display: flex; justify-content: space-between; padding: 3px 6px; font-size: 6px; }
  .app-mark { position: absolute; left: 50%; top: 120px; transform: translateX(-50%); width: 40px; height: 40px; border-radius: 50%; border: 3px solid var(--white); }
  .app-name { position: absolute; top: 213px; width: 100%; text-align: center; font-size: 12px; font-weight: 500; letter-spacing: 6px; padding-left: 6px; }
  .app-tag { position: absolute; top: 238px; width: 100%; text-align: center; font-size: 7px; }
</style>
</head>
<body>
<div class="page">
  <header class="topbar">
    <div class="brand"><span class="brand-dot"></span>Marlowick</div>
    <ul class="nav">
      <li><a class="is-current" href="#">Home</a></li>
      <li><a href="#">Download</a></li>
      <li><a href="#">Sign Up</a></li>
      <li><a href="#">Contact</a></li>
      <li><a href="#">About</a></li>
    </ul>
  </header>

  <div class="hero-photo" role="img" aria-label="Photo of smiling students gathered around a tablet and phones in a classroom"></div>
  <div class="hero-fade"></div>

  <p class="hero-copy">Lorem ipsum dolor sit amet, consectetuer adipiscing elit, sed diam nonummy nibh euismod</p>
  <a class="btn btn-login" href="#">LOG IN</a>
  <p class="signup-hint">Don’t have account?</p>
  <a class="btn btn-signup" href="#">Sign Up</a>

  <div class="phone">
    <span class="phone-dot"></span>
    <span class="phone-cam"></span>
    <span class="phone-speaker"></span>
    <div class="screen">
      <div class="status"><span>●●●●●</span><span>11:47</span><span>86%</span></div>
      <span class="app-mark"></span>
      <div class="app-name">MARLOWICK</div>
      <div class="app-tag">SECURITY THROUGH TRANPARENCY</div>
    </div>
  </div>
</div>
</body>
</html>
```